Billboard design for a jewelry store.

I am looking for a very unique design with a catchy slogan, I am looking for billboard so good that will make the front page of the newspaper. I want to target customers that are looking for diamond jewelry or diamonds in general. For sure not interested in anything that is genetic or been used in the past. I want the billboard to stand out and very unique. Text not more than 3 words, our logo and an image.

Target Market(s)

Local

Industry/Entity Type

Jewelry Store

Font styles to use
Other font styles liked:
• Open to your suggestion for the font.

Requirements
Must have
• Unique, very brief a catchy slogan. My logo and an image. Open for suggestions. I want also different formats to use on social media.
Nice to have
• I am open to unique and amazing new ideas. I don't want general used design or slogan.
Should not have
• Too much text

```html
<!DOCTYPE html>
<html lang="en">
<head>
<meta charset="UTF-8">
<title>Vella Jewelers – Billboard</title>
<link href="https://fonts.googleapis.com/css2?family=Roboto+Condensed:wght@300&display=swap" rel="stylesheet">
<style>
  :root {
    --page-bg: #ffffff;
    --plum-deep: #3a1450;
    --plum-mid: #5a1a66;
    --plum-bright: #7c1f74;
    --band-violet: #4b1b80;
    --accent-magenta: #9c2a8f;
    --accent-violet: #4a1c86;
    --photo-light: #f7f1ec;
    --photo-skin: #e6bfa6;
    --text-white: #ffffff;
  }
  * { margin: 0; padding: 0; box-sizing: border-box; }
  html, body {
    width: 1200px;
    height: 1200px;
    overflow: hidden;
    background: var(--page-bg);
  }
  .billboard {
    position: absolute;
    left: 40px;
    top: 437px;
    width: 1120px;
    height: 326px;
    overflow: hidden;
    box-shadow: 0 10px 18px rgba(0, 0, 0, 0.28);
  }
  .billboard-shapes {
    position: absolute;
    inset: 0;
    width: 100%;
    height: 100%;
  }
  .brand-name {
    position: absolute;
    left: 66px;
    top: 82px;
    width: 680px;
    color: var(--text-white);
    font-family: "Roboto Condensed", sans-serif;
    font-weight: 300;
    font-size: 96px;
    line-height: 1;
    letter-spacing: 0;
    white-space: nowrap;
  }
  .slogan {
    position: absolute;
    right: 362px;
    top: 279px;
    color: var(--text-white);
    font-family: "Roboto Condensed", sans-serif;
    font-weight: 300;
    font-size: 38px;
    line-height: 1;
    white-space: nowrap;
  }
</style>
</head>
<body>
  <section class="billboard">
    <svg class="billboard-shapes" viewBox="0 0 1120 326" preserveAspectRatio="none">
      <defs>
        <linearGradient id="plumGradient" x1="0" y1="0" x2="0" y2="1">
          <stop offset="0" stop-color="var(--plum-deep)"/>
          <stop offset="0.55" stop-color="var(--plum-mid)"/>
          <stop offset="1" stop-color="var(--plum-bright)"/>
        </linearGradient>
        <linearGradient id="photoGradient" x1="0" y1="0" x2="1" y2="0">
          <stop offset="0" stop-color="var(--photo-light)"/>
          <stop offset="0.45" stop-color="var(--photo-skin)"/>
          <stop offset="1" stop-color="var(--photo-light)"/>
        </linearGradient>
      </defs>
      <rect class="panel-plum" x="0" y="0" width="1120" height="326" fill="url(#plumGradient)"/>
      <rect class="band-slogan" x="0" y="269" width="1120" height="57" fill="var(--band-violet)"/>
      <path class="accent-magenta" d="M770 0 H820 C790 90 800 200 860 326 H830 C780 220 765 110 770 0 Z" fill="var(--accent-magenta)"/>
      <path class="accent-violet" d="M790 0 H830 C805 100 815 210 880 326 H840 C790 220 780 110 790 0 Z" fill="var(--accent-violet)"/>
      <path class="photo-area" role="img" aria-label="Photo of a woman covering her eyes with her hands, wearing colourful gemstone rings and red nail polish"
            d="M825 0 H1120 V326 H885 C820 210 805 100 825 0 Z" fill="url(#photoGradient)"/>
    </svg>
    <h1 class="brand-name">Vella Jewelers</h1>
    <p class="slogan">Love. Timeless. Beautiful.</p>
  </section>
</body>
</html>
```